Harbourline Works Group Business Card Redesign

Logo has already been developed. The current business card is one sided. We'd like our mission on the back and more creativity so it pops. We may also like a tagline on the back
One call...all the service, all the savings. Examples are attached from our printer but we don't like them. The front is how we have our existing cards but the back is new. We are open to all ideas. We do like our colors/ brand of purple, black, white...

```html
<!DOCTYPE html>
<html lang="en">
<head>
<meta charset="utf-8">
<title>Harbourline Works Group – Business Card</title>
<link rel="stylesheet" href="https://fonts.googleapis.com/css2?family=Crimson+Pro:wght@400;600&display=swap">
<style>
  :root {
    --purple: #6a2c91;
    --ink: #333333;
    --charcoal: #3a3a3a;
    --paper: #f6f7f7;
    --backdrop: #e4e4e4;
    --white: #ffffff;
  }
  * { margin: 0; padding: 0; box-sizing: border-box; }
  html, body { width: 1200px; height: 435px; overflow: hidden; }
  body {
    background: var(--backdrop);
    font-family: "Crimson Pro", Georgia, serif;
    color: var(--ink);
    position: relative;
  }
  .card {
    position: absolute;
    top: 72px;
    width: 525px;
    height: 300px;
    background: var(--paper);
    transform: scale(0.9677);
    transform-origin: top left;
    box-shadow: 0 6px 14px rgba(0,0,0,0.18);
    overflow: hidden;
  }
  .card--front { left: 47px; }
  .card--back { left: 615px; }
  .bands { position: absolute; left: 0; top: 0; width: 525px; height: 300px; }

  .brand {
    position: absolute;
    left: 118px;
    top: 58px;
    display: flex;
    align-items: center;
    gap: 12px;
  }
  .brand__dot {
    width: 26px; height: 26px; border-radius: 50%;
    background: var(--purple);
    flex: none;
  }
  .brand__name {
    font-size: 25px;
    font-weight: 600;
    color: var(--purple);
    line-height: 1;
  }
  .brand__tagline {
    position: absolute;
    left: 156px;
    top: 88px;
    font-size: 14px;
    font-weight: 600;
    color: var(--ink);
  }

  .name, .role {
    position: absolute;
    top: 142px;
    height: 36px;
    line-height: 36px;
    font-size: 17px;
    color: var(--white);
    white-space: nowrap;
  }
  .name { left: 88px; }
  .role { left: 285px; }

  .contact {
    position: absolute;
    left: 0; right: 0;
    top: 228px;
    text-align: center;
    font-size: 16px;
    line-height: 21px;
    color: var(--ink);
  }
  .contact__row { display: flex; justify-content: center; align-items: center; gap: 14px; }
  .contact__item { display: inline-flex; align-items: center; gap: 4px; }
  .icon { width: 12px; height: 12px; fill: var(--ink); }

  .mission {
    position: absolute;
    left: 0;
    width: 252px;
    top: 107px;
    text-align: center;
    color: var(--white);
    font-size: 13px;
    line-height: 16.5px;
    white-space: nowrap;
  }
  .mission__title { font-size: 16px; line-height: 18px; margin-bottom: 1px; }
  .slogan {
    position: absolute;
    left: 290px;
    width: 225px;
    top: 133px;
    text-align: center;
    color: var(--white);
    font-size: 14.5px;
    line-height: 17px;
  }
</style>
</head>
<body>
  <section class="card card--front" aria-label="Card front">
    <svg class="bands" viewBox="0 0 525 300" aria-hidden="true">
      <polygon points="0,142 273,142 240,178 0,178" fill="var(--charcoal)"/>
      <polygon points="287,142 525,142 525,178 254,178" fill="var(--purple)"/>
    </svg>
    <div class="brand">
      <span class="brand__dot"></span>
      <span class="brand__name">Harbourline Works Group</span>
    </div>
    <p class="brand__tagline">Delivering Results. Creating Savings.</p>
    <p class="name">Daniel Marsh</p>
    <p class="role">Business Development Manager</p>
    <div class="contact">
      <div class="contact__row">
        <span class="contact__item">
          <svg class="icon" viewBox="0 0 12 12"><path d="M2.4 0.8 4.2 2.9 3.2 4.3c.7 1.6 2 2.9 3.6 3.6l1.4-1 2.1 1.8-1 2c-4.4-.3-8-3.9-8.3-8.3z"/></svg>480 555 0142
        </span>
        <span class="contact__item">
          <svg class="icon" viewBox="0 0 12 12"><rect x="3" y="0.5" width="6" height="3"/><rect x="0.5" y="4" width="11" height="5" rx="1"/><rect x="3" y="8" width="6" height="3.5"/></svg>44 7700 900 318
        </span>
        <span class="contact__item">
          <svg class="icon" viewBox="0 0 12 12"><rect x="3" y="0.5" width="6" height="11" rx="1"/><rect x="4" y="2" width="4" height="5" fill="var(--paper)"/></svg>480 555 0197
        </span>
      </div>
      <div>1840 W. Ridgeview Road, Suite 200, Mesa, AZ 85201</div>
      <div class="contact__row">
        <span class="contact__item">
          <svg class="icon" viewBox="0 0 12 12"><rect x="0.5" y="2" width="11" height="8"/><path d="M1 2.5 6 6.5 11 2.5" fill="none" stroke="var(--paper)" stroke-width="1"/></svg>dmarsh@harbourlineworks.com
        </span>
      </div>
    </div>
  </section>

  <section class="card card--back" aria-label="Card back">
    <svg class="bands" viewBox="0 0 525 300" aria-hidden="true">
      <polygon points="0,100 275,100 241,200 0,200" fill="var(--charcoal)"/>
      <polygon points="288,100 525,100 525,200 253,200" fill="var(--purple)"/>
    </svg>
    <div class="mission">
      <p class="mission__title">Our Mission</p>
      <p>To ensure the injured worker returns to<br>function and work, faster, better, stronger<br>while creating lonterm client loyalty<br>through service and value we provide</p>
    </div>
    <p class="slogan">One call...all the service,<br>all the savings</p>
  </section>
</body>
</html>
```